Copper Ridge Business Cards For New Startup

I am looking for you to design some business cards for a new startup https://copperridgehub.example. I have supplied logo, brand guidelines and our signatures as a guide.

We need this to reflect the brand guidelines and the website for brand consistency,

What is Copper Ridge?

Mallorca's Business Growth Community
Join your new business community full of passionate entrepreneurs who
love to solve problems and help each other grow together!

Any questions you can ask.

Target Market(s)

Business to Business

Contact Information for Business Card

These are attached (signatures) to the job

Font styles to use
Other font styles liked:
• Open Sans

Requirements
Must have
• Match design guidelines
Nice to have
• Photos of our faces so people remember us

```html
<!DOCTYPE html>
<html lang="en">
<head>
<meta charset="utf-8">
<title>Copper Ridge – Business Card</title>
<link rel="stylesheet" href="https://fonts.googleapis.com/css2?family=Open+Sans:wght@400;600;700&display=swap">
<style>
  :root {
    --brand-green: #676a2e;
    --card-light: #e8f3f3;
    --ink: #222222;
    --backdrop: #d9d4cc;
    --photo-light: #dfe4e2;
    --photo-dark: #9a8f86;
  }
  * { box-sizing: border-box; margin: 0; padding: 0; }
  html, body {
    width: 900px; height: 1200px; overflow: hidden;
    background: var(--backdrop);
    font-family: "Open Sans", Arial, sans-serif;
  }
  .canvas { position: relative; width: 900px; height: 1200px; }

  .card { position: absolute; left: 86px; width: 736px; height: 430px; }

  /* Front */
  .card-front { top: 136px; background: var(--card-light); }
  .identity-band {
    position: absolute; left: 26px; top: 25px; width: 684px; height: 268px;
    background: var(--brand-green);
  }
  .portrait {
    position: absolute; left: 34px; top: 34px; width: 200px; height: 200px;
    border-radius: 50%; border: 8px solid var(--card-light);
    background: radial-gradient(circle at 50% 40%, var(--photo-dark) 0 30%, var(--photo-light) 62%);
  }
  .identity-text { position: absolute; left: 295px; top: 96px; color: var(--card-light); }
  .person-name { font-size: 30px; font-weight: 700; line-height: 1.2; }
  .person-role { font-size: 21px; font-weight: 400; line-height: 1.3; }

  .contact-row {
    position: absolute; left: 0; right: 0; top: 317px;
    display: flex; justify-content: center; align-items: flex-end;
  }
  .contact-item { display: flex; flex-direction: column; align-items: center; gap: 10px; padding: 0 14px; }
  .contact-icon {
    width: 42px; height: 42px; border-radius: 50%; background: var(--brand-green);
    display: flex; align-items: center; justify-content: center;
  }
  .contact-text { font-size: 19px; color: var(--ink); line-height: 1.3; white-space: nowrap; }
  .contact-divider { width: 3px; height: 34px; background: var(--ink); margin-bottom: 4px; }

  /* Back */
  .card-back { top: 632px; background: var(--brand-green); }
  .brand-lockup {
    position: absolute; left: 72px; top: 124px;
    display: flex; align-items: center; gap: 42px;
  }
  .brand-mark { width: 128px; height: 128px; border-radius: 50%; border: 3px solid var(--card-light); }
  .brand-name {
    font-size: 58px; font-weight: 600; color: var(--card-light);
    letter-spacing: 0.5px; white-space: nowrap;
  }
  .social-row {
    position: absolute; left: 0; right: 0; top: 348px;
    display: flex; justify-content: center; gap: 22px;
  }
  .social-dot { width: 48px; height: 48px; border-radius: 50%; background: var(--card-light); }
</style>
</head>
<body>
<main class="canvas">

  <section class="card card-front" aria-label="Business card front">
    <div class="identity-band">
      <div class="portrait" role="img" aria-label="Portrait photo of Daniel Morrow"></div>
      <div class="identity-text">
        <h1 class="person-name">Daniel Morrow</h1>
        <p class="person-role">Founder &amp; Growth Hacker</p>
      </div>
    </div>

    <div class="contact-row">
      <div class="contact-item">
        <span class="contact-icon">
          <svg width="18" height="26" viewBox="0 0 18 26" aria-hidden="true">
            <rect x="2" y="1.5" width="14" height="23" rx="2" fill="none" stroke="#e8f3f3" stroke-width="2"/>
            <rect x="5" y="5" width="8" height="13" fill="#e8f3f3"/>
            <circle cx="9" cy="21" r="1.3" fill="#e8f3f3"/>
          </svg>
        </span>
        <span class="contact-text">+34 611 482 730</span>
      </div>
      <span class="contact-divider"></span>
      <div class="contact-item">
        <span class="contact-icon">
          <svg width="24" height="18" viewBox="0 0 24 18" aria-hidden="true">
            <rect x="1" y="1" width="22" height="16" rx="1.5" fill="#e8f3f3"/>
            <path d="M1.5 2 L12 10 L22.5 2" fill="none" stroke="#676a2e" stroke-width="1.8"/>
          </svg>
        </span>
        <span class="contact-text">dm@copperridgehub.example</span>
      </div>
      <span class="contact-divider"></span>
      <div class="contact-item">
        <span class="contact-icon">
          <svg width="24" height="24" viewBox="0 0 24 24" aria-hidden="true" fill="none" stroke="#e8f3f3" stroke-width="1.6">
            <circle cx="12" cy="12" r="10"/>
            <ellipse cx="12" cy="12" rx="4.5" ry="10"/>
            <line x1="2" y1="12" x2="22" y2="12"/>
            <line x1="3.5" y1="7" x2="20.5" y2="7"/>
            <line x1="3.5" y1="17" x2="20.5" y2="17"/>
          </svg>
        </span>
        <span class="contact-text">copperridgehub.example</span>
      </div>
    </div>
  </section>

  <section class="card card-back" aria-label="Business card back">
    <div class="brand-lockup">
      <span class="brand-mark" aria-hidden="true"></span>
      <span class="brand-name">COPPER RIDGE</span>
    </div>
    <div class="social-row" aria-label="Social media links">
      <span class="social-dot"></span>
      <span class="social-dot"></span>
      <span class="social-dot"></span>
      <span class="social-dot"></span>
      <span class="social-dot"></span>
    </div>
  </section>

</main>
</body>
</html>
```